update and create new Sorvane Dojo Karate Website

We require a new and modernised website for our Karate school.
Website currently is www.Sorvanedojo.example
Please check the current state of the website to start off with.
The basis of the brief attached is to provide context on what we want for the new website.

1) Please read through the build brief attached.
2) We are looking for a vendor who can service our organisation's website needs in future and ongoing.
3) Our budget is more than currently able to post on here and is subject to discussion should we choose you as our vendor. The amount initially is priced to be between $700.00 - $1000.00 AUD for the selected website.
4) easy and simple use and communication is a must.
5) this build request is subject to updating should we require further needs on the website.
6) The reason we have chosen the "refundable" option at this stage is because we've never used Pixel Forum before. However the winning vendor will receive full commission and continued pay ongoing for future management of the website.

Thank you
Milo
Updates

Hi Designers and Vendors Regarding this website. Our budget is set at approx. $1000.00 with ongoing work commission to run the website. I advise you read what is re

Industry/Entity Type

Communication

```html
<!DOCTYPE html>
<html lang="en">
<head>
<meta charset="utf-8">
<title>Sorvane Dojo Karate — News</title>
<link rel="stylesheet" href="https://fonts.googleapis.com/css2?family=Oswald:wght@400;500;600&family=Open+Sans:wght@300;400&display=swap">
<style>
  :root {
    --page-bg: #000000;
    --header-bg-top: #353535;
    --header-bg-bottom: #262626;
    --title: #ffffff;
    --subtitle: #b9b9b9;
    --nav-text: #c8c8c8;
    --nav-active: #ffffff;
    --nav-border: #d8d8d8;
    --card-bg: #333333;
    --card-bg-active: #777777;
    --card-heading: #e6e6e6;
    --card-text: #e2e2e2;
    --accent: #8fbde6;
  }
  * { box-sizing: border-box; margin: 0; padding: 0; }
  html, body {
    width: 1200px;
    height: 1000px;
    overflow: hidden;
    background: var(--page-bg);
  }
  .site-header {
    height: 160px;
    background: linear-gradient(180deg, var(--header-bg-top), var(--header-bg-bottom));
    text-align: center;
    padding-top: 26px;
  }
  .site-title {
    font-family: "Oswald", sans-serif;
    font-weight: 600;
    font-size: 44px;
    line-height: 56px;
    color: var(--title);
    text-transform: uppercase;
    letter-spacing: -0.5px;
  }
  .site-intro {
    width: 960px;
    margin: 6px auto 0;
    font-family: "Open Sans", sans-serif;
    font-weight: 300;
    font-size: 20.5px;
    line-height: 25px;
    color: var(--subtitle);
    letter-spacing: -0.3px;
  }
  .main-nav {
    display: flex;
    height: 50px;
    border-top: 1px solid var(--nav-border);
    border-bottom: 1px solid var(--nav-border);
  }
  .main-nav a {
    flex: 1;
    display: flex;
    align-items: center;
    justify-content: center;
    font-family: "Oswald", sans-serif;
    font-size: 15px;
    color: var(--nav-text);
    text-decoration: none;
    text-transform: uppercase;
    border-left: 1px solid var(--nav-border);
  }
  .main-nav a:first-child { border-left: none; }
  .main-nav a.is-current { color: var(--nav-active); }
  .news-grid {
    width: 960px;
    margin: 55px auto 0;
    display: grid;
    grid-template-columns: repeat(3, 310px);
    column-gap: 15px;
    row-gap: 43px;
  }
  .news-card {
    position: relative;
    height: 295px;
    background: var(--card-bg);
    padding: 28px 19px 0;
  }
  .news-card.is-highlighted { background: var(--card-bg-active); }
  .news-card h2 {
    font-family: "Oswald", sans-serif;
    font-weight: 400;
    font-size: 21px;
    line-height: 28px;
    color: var(--card-heading);
    letter-spacing: -0.6px;
    margin-bottom: 4px;
  }
  .news-card p {
    font-family: "Open Sans", sans-serif;
    font-size: 12px;
    line-height: 17px;
    color: var(--card-text);
    margin-bottom: 17px;
  }
  .more-button {
    position: absolute;
    left: 19px;
    bottom: 19px;
    width: 109px;
    height: 32px;
    border: 2px solid var(--accent);
    display: flex;
    align-items: center;
    justify-content: center;
    font-family: "Oswald", sans-serif;
    font-size: 13px;
    color: var(--accent);
    text-decoration: none;
  }
</style>
</head>
<body>
  <header class="site-header">
    <h1 class="site-title">Sorvane Dojo Karate</h1>
    <p class="site-intro">Welcome to Sorvane Dojo Karate, to our Dojo and to our events as we invite all Karate-ka and visitors world-wide to experience what we do and invite them to part-take in our Karate activities.</p>
  </header>

  <nav class="main-nav">
    <a href="#">Home</a>
    <a href="#">About</a>
    <a href="#" class="is-current">News</a>
    <a href="#">Dojo</a>
    <a href="#">Get Started</a>
    <a href="#">Contact</a>
  </nav>

  <main class="news-grid">
    <article class="news-card">
      <h2>Tournaments</h2>
      <p>In mollis erat mattisy neque facilisis, sit amet ultricieser erarutrum. Cras facilisis, nulla vel viverra auctor, leo magna sodales felis, quis malesuada nibh odio ut velit. Proin pharetra luctus.</p>
      <p>Maecenas vehiculaegestas venenatis. Duiser massa elit, auctor pellentesque vel, aliquet amet erat.</p>
      <a class="more-button" href="#">more</a>
    </article>
    <article class="news-card">
      <h2>Events</h2>
      <p>In mollis erat mattisy neque facilisis, sit amet ultricieser erarutrum. Cras facilisis, nulla vel viverra auctor, leo magna sodales felis, quis malesuada nibh odio ut velit. Proin pharetra luctus.</p>
      <p>Maecenas vehiculaegestas venenatis. Duiser massa elit, auctor pellentesque vel, aliquet amet erat.</p>
      <a class="more-button" href="#">more</a>
    </article>
    <article class="news-card">
      <h2>JAPAN 日本</h2>
      <p>In mollis erat mattisy neque facilisis, sit amet ultricieser erarutrum. Cras facilisis, nulla vel viverra auctor, leo magna sodales felis, quis malesuada nibh odio ut velit. Proin pharetra luctus.</p>
      <p>Maecenas vehiculaegestas venenatis. Duiser massa elit, auctor pellentesque vel, aliquet amet erat.</p>
      <a class="more-button" href="#">more</a>
    </article>
    <article class="news-card">
      <h2>Sorvane Dojo Activities</h2>
      <p>In mollis erat mattisy neque facilisis, sit amet ultricieser erarutrum. Cras facilisis, nulla vel viverra auctor, leo magna sodales felis, quis malesuada nibh odio ut velit. Proin pharetra luctus.</p>
      <p>Maecenas vehiculaegestas venenatis. Duiser massa elit, auctor pellentesque vel, aliquet amet erat.</p>
      <a class="more-button" href="#">more</a>
    </article>
    <article class="news-card is-highlighted">
      <h2>Affiliations</h2>
      <p>In mollis erat mattisy neque facilisis, sit amet ultricieser erarutrum. Cras facilisis, nulla vel viverra auctor, leo magna sodales felis, quis malesuada nibh odio ut velit. Proin pharetra luctus.</p>
      <p>Maecenas vehiculaegestas venenatis. Duiser massa elit, auctor pellentesque vel, aliquet amet erat.</p>
      <a class="more-button" href="#">more</a>
    </article>
    <article class="news-card">
      <h2>Social Media</h2>
      <p>In mollis erat mattisy neque facilisis, sit amet ultricieser erarutrum. Cras facilisis, nulla vel viverra auctor, leo magna sodales felis, quis malesuada nibh odio ut velit. Proin pharetra luctus.</p>
      <p>Maecenas vehiculaegestas venenatis. Duiser massa elit, auctor pellentesque vel, aliquet amet erat.</p>
      <a class="more-button" href="#">more</a>
    </article>
    <article class="news-card">
      <h2>Links</h2>
    </article>
    <article class="news-card">
      <h2>Our Core Values</h2>
    </article>
    <article class="news-card">
      <h2>Calendar</h2>
    </article>
  </main>
</body>
</html>
```